**Launching Worlds Greatest Eco Friendly Doggy Poop Bags!**

We are an eco-friendly company located in San Francisco, California. We are launching a new line of amazing new eco-friendly doggy poop bags. They are biodegradable and super easy to open. Additionally they are strong, durable and light weight. We would like to see some designs for a box and logo under the label "Bright Meadow". We'd like to see the colors green and blue used to promote earth friendly product.

Target Market(s)

Dog owners

Industry/Entity Type

It Company

Colors
00a990
0592cd
9bcb3c

Requirements
Must have
• Would like to see a happy looking dog and portray earth friendly images. Cartoon type images. Would like fun, happy, cartoon like dog and Bright Meadow Logo to go in front of the box.
Nice to have
• Images of dog prints or happy dog(s) that we can put in different areas of the box. (examples of competitors boxes included)
Should not have
• Not fancy or formal.

```html
<!DOCTYPE html>
<html lang="en">
<head>
<meta charset="utf-8">
<title>Bright Meadow – eco-friendly doggy poop bags</title>
<link rel="stylesheet" href="https://fonts.googleapis.com/css2?family=Glegoo&family=Courgette&display=swap">
<style>
  :root {
    --kraft: #cfb07a;
    --kraft-light: #d9bc82;
    --band: #fdf4e3;
    --band-dot: #e6dccb;
    --teal: #00a990;
    --blue: #0592cd;
    --ink: #2f2a24;
    --gold: #c4a05c;
    --gold-light: #d4b374;
    --pill-text: #fff8ea;
  }
  html, body {
    margin: 0;
    padding: 0;
    overflow: hidden;
    background: #ffffff;
  }
  .box-front {
    position: relative;
    width: 870px;
    height: 1200px;
    overflow: hidden;
    font-family: "Glegoo", Georgia, serif;
    color: var(--ink);
  }
  .kraft-pattern {
    position: absolute;
    inset: 0;
    background: radial-gradient(circle at 50% 45%, var(--kraft-light), var(--kraft));
  }
  .size-label {
    position: absolute;
    left: 41px;
    top: 70px;
    margin: 0;
    font-size: 28px;
    line-height: 41px;
    text-align: center;
  }
  .brand-band {
    position: absolute;
    left: 0;
    top: 340px;
    width: 870px;
    height: 240px;
    background: var(--band);
  }
  .brand-band::before,
  .brand-band::after {
    content: "";
    position: absolute;
    left: 0;
    right: 0;
    height: 14px;
    background: radial-gradient(circle at 12px 7px, var(--band) 9px, transparent 10px) repeat-x;
    background-size: 24px 14px;
  }
  .brand-band::before { top: -9px; }
  .brand-band::after { bottom: -9px; }
  .band-dots {
    position: absolute;
    left: 8px;
    right: 8px;
    height: 0;
    border-top: 5px dotted var(--band-dot);
  }
  .band-dots.top { top: 9px; }
  .band-dots.bottom { bottom: 9px; }
  .brand-name {
    position: absolute;
    left: 0;
    right: 0;
    top: 62px;
    margin: 0;
    text-align: center;
    font-family: "Glegoo", Georgia, serif;
    font-weight: 400;
    font-size: 84px;
    line-height: 110px;
    color: var(--teal);
  }
  .tagline {
    position: absolute;
    left: 123px;
    top: 627px;
    width: 619px;
    height: 72px;
    border-radius: 36px;
    background: var(--teal);
    color: var(--pill-text);
    font-family: "Courgette", cursive;
    font-size: 37px;
    line-height: 72px;
    text-align: center;
    margin: 0;
  }
  .benefits {
    position: absolute;
    left: 0;
    right: 0;
    top: 742px;
    margin: 0;
    padding: 0;
    list-style: none;
    text-align: center;
    font-size: 27px;
    line-height: 42px;
  }
  .benefits li::before {
    content: "❦ ";
  }
  .value-badge {
    position: absolute;
    left: 45px;
    top: 970px;
    width: 250px;
    height: 250px;
  }
  .value-badge-text {
    position: absolute;
    left: 45px;
    top: 1030px;
    width: 250px;
    margin: 0;
    text-align: center;
    font-size: 27px;
    line-height: 36px;
  }
  .value-badge-text strong {
    font-weight: 700;
    display: block;
  }
  .warning {
    position: absolute;
    left: 510px;
    top: 1040px;
    width: 310px;
    margin: 0;
    text-align: center;
    font-size: 21px;
    line-height: 28px;
  }
  .warning-title {
    display: block;
    font-size: 29px;
    line-height: 38px;
  }
</style>
</head>
<body>
  <main class="box-front">
    <div class="kraft-pattern" role="img" aria-label="Kraft paper background with a repeating pattern of yellow paw prints and dog bones"></div>

    <p class="size-label">Standard bags<br>Sacs standards<br>Boisas estandar</p>

    <section class="brand-band">
      <div class="band-dots top"></div>
      <h1 class="brand-name">Bright Meadow</h1>
      <div class="band-dots bottom"></div>
    </section>

    <p class="tagline">eco-friendly doggy poop bags.</p>

    <ul class="benefits">
      <li>100% eco-friendly</li>
      <li>Biodegradable and super easy to open.</li>
      <li>Strong, durable and light weight.</li>
    </ul>

    <svg class="value-badge" viewBox="0 0 250 250" role="img" aria-label="Gold circular value pack badge with a faint globe illustration">
      <circle cx="125" cy="125" r="123" fill="var(--gold)"/>
      <circle cx="125" cy="125" r="110" fill="var(--gold-light)"/>
    </svg>
    <p class="value-badge-text"><strong>Value Pack</strong>Format ECONO<br>ECONO<br>PACK</p>

    <p class="warning"><span class="warning-title">WARNING</span>CHOKING HAZARD<br>Please Keep away from<br>Children</p>
  </main>
</body>
</html>
```